Data/Computer Security company needs a brochure design

We need a brochure design for Vault Glimmer.
We deliver security solutions that manage critical risks, protect vital information and provide regulatory compliance. (mostly professional offices and small businesses with an emphasis in financial services) Optimal security is achieved through agent-based auditing and network activity monitoring.
Specialists in the area of helping Broker/Dealers and Independent Financial Service Representatives measure field office security, threat readiness and compliance with current policies and procedures. We provide auditors with clear, concise reports of policy deviations along with guidance in closing gaps, weaknesses or deficiencies.
Our services allow audit staff efficiency and productivity in their process while ensuring the field offices are utilizing best security practices and exercising the appropriate level of diligence and care in protecting the client information entrusted to them.
More about process and services can be seen on our website - www.vaultglimmer-example.com
We use blues and grays in our designs.
Industry/Entity Type
Financial
Look and feel
Each slider illustrates characteristics of the customer's brand and the style your logo design should communicate.

```html
<!DOCTYPE html>
<html lang="en">
<head>
<meta charset="utf-8">
<title>Vault Glimmer – Brochure Spread</title>
<link rel="stylesheet" href="https://fonts.googleapis.com/css2?family=Ubuntu:wght@300;400;500;700&family=Open+Sans:wght@400;600;700&display=swap">
<style>
  :root {
    --backdrop: #2b2b2d;
    --photo-light: #b9b6b1;
    --photo-mid: #8a8783;
    --photo-dark: #3c3b3a;
    --panel-grey: rgba(92, 90, 88, 0.8);
    --panel-text: #ecebe9;
    --heading-white: #f4f4f4;
    --sheet-white: #ffffff;
    --brand-blue: #2f9ad8;
    --network-blue: #6fb7e6;
    --box-text: #ffffff;
  }
  * { box-sizing: border-box; margin: 0; padding: 0; }
  html, body {
    width: 1200px; height: 793px; overflow: hidden;
    background: var(--backdrop);
  }
  .spread {
    position: absolute; left: 30px; top: 92px;
    width: 1140px; height: 610px;
    background: var(--sheet-white);
    overflow: hidden;
    font-family: "Open Sans", Arial, sans-serif;
  }
  .photo-area {
    position: absolute; left: 0; top: 0; width: 795px; height: 610px;
    background:
      radial-gradient(ellipse at 45% 35%, var(--photo-light) 0%, var(--photo-mid) 45%, transparent 75%),
      linear-gradient(180deg, #a9a6a1 0%, #8f8c88 55%, var(--photo-dark) 100%);
  }
  .questions {
    position: absolute; left: 40px; top: 82px;
    font-family: "Ubuntu", Arial, sans-serif; color: var(--heading-white);
  }
  .questions p { font-size: 15px; font-weight: 300; letter-spacing: .5px; margin-bottom: 44px; }
  .questions strong { font-size: 21px; font-weight: 700; }
  .brand-name {
    position: absolute; left: 36px; bottom: 30px;
    display: flex; align-items: center; gap: 8px;
    font-family: "Ubuntu", Arial, sans-serif; font-weight: 700;
    font-size: 19px; color: var(--heading-white);
  }
  .brand-name .dot { width: 12px; height: 12px; border-radius: 50%; background: var(--heading-white); }
  .facts-panel {
    position: absolute; left: 573px; top: 18px; width: 214px; height: 574px;
    background: var(--panel-grey); border-radius: 10px;
    padding: 11px 11px; color: var(--panel-text);
    font-size: 7.2px; line-height: 1.32;
    overflow: hidden;
  }
  .facts-panel h3 { font-size: 8.2px; font-weight: 700; margin: 8px 0 3px; letter-spacing: .2px; }
  .facts-panel h3:first-child { margin-top: 0; }
  .facts-panel ul { list-style: none; }
  .facts-panel li { padding-left: 8px; position: relative; margin-bottom: 2px; }
  .facts-panel li::before { content: "–"; position: absolute; left: 0; }
  .facts-panel p { margin-bottom: 3px; }
  .network-art {
    position: absolute; left: 795px; top: 0; width: 345px; height: 610px;
    background:
      radial-gradient(ellipse at 95% 85%, var(--network-blue) 0%, rgba(111,183,230,.45) 30%, transparent 60%),
      radial-gradient(ellipse at 100% 10%, rgba(111,183,230,.5) 0%, transparent 40%),
      var(--sheet-white);
  }
  .help-box {
    position: absolute; left: 806px; top: 18px; width: 322px; height: 556px;
    background: var(--brand-blue); border-radius: 8px;
    padding: 12px 13px; color: var(--box-text);
    font-size: 7.9px; line-height: 1.36;
    overflow: hidden;
  }
  .help-box h2 {
    font-family: "Ubuntu", Arial, sans-serif; font-weight: 700;
    font-size: 25px; line-height: 1.05; letter-spacing: .3px;
  }
  .help-box h2 span { display: block; font-weight: 300; font-size: 25px; margin-bottom: 14px; }
  .help-box p { margin-bottom: 8px; }
  .help-box b { font-weight: 700; }
</style>
</head>
<body>
  <main class="spread">
    <div class="photo-area" role="img" aria-label="Photograph of a frustrated businessman in glasses and tie working at a laptop, in grey tones"></div>
    <div class="network-art" role="img" aria-label="Decorative blue network of connected nodes and lines"></div>

    <div class="questions">
      <p><strong>HOW BIG</strong> is the problem?</p>
      <p><strong>WHY</strong> do they do it?</p>
      <p><strong>HOW</strong> do they do it?</p>
    </div>

    <div class="brand-name"><span class="dot"></span>Vault Glimmer</div>

    <section class="facts-panel">
      <h3>HOW BIG IS THE PROBLEM?</h3>
      <ul>
        <li>Anti-virus vendors report receiving 60,000 new malware samples every day</li>
        <li>Approximately 1500 new malware sites are created per day</li>
        <li>Sixty percent of top Searchly search terms return malicious sites within the first 100 results</li>
      </ul>
      <h3>WHY DO THEY DO IT?</h3>
      <ul>
        <li>Northern Pharmacy spam campaign earned $16,000 per day</li>
        <li>Affiliate webmasters redirecting to a scareware site can earn $5,000 per week</li>
        <li>Credit card information sells for $1.35 to $200 per card</li>
        <li>Botnet rental runs as little as $10 - $60 per hour</li>
        <li>One million email addresses can be purchased for $20 - $100</li>
        <li>A complete set of data on a US resident is only $5 to $8</li>
        <li>A continuous 24-hour Botnet for DDoS attacks can be launched for as little as $50</li>
        <li>Online bank account details go for $5 to $1,500 depending on level of detail and balance</li>
      </ul>
      <h3>HOW DO THEY DO IT?</h3>
      <p>They do it by exploiting weaknesses in common software like DeskWorks Office, DocuView Reader, FlashPlay and Javelin. Software developers have created "corrective" applications designed to patch known weaknesses in software on the target computer. The malware is delivered in numerous ways:</p>
      <ul>
        <li>A pop-up in your web browser saying you have a virus</li>
        <li>An email or personal DeskWorks Office email attachment</li>
        <li>A link in a FriendSpace message</li>
        <li>A link in your Searchly search results</li>
        <li>A contaminated USB drive</li>
        <li>Inside a free game or download</li>
        <li>Poisoned ads on prominent websites</li>
        <li>Through security weaknesses in old, un-patched software</li>
      </ul>
    </section>

    <section class="help-box">
      <h2>HOW WE HELP YOU<span>PROTECT YOURSELF</span></h2>
      <p>Vault Glimmer has assembled a program to help you understand and manage your risks, reducing your exposure and cost to business interruption and response.</p>
      <p><b>1. PATCH MANAGEMENT</b> – Utilizing the same tools used by the Military, we monitor the applications installed on each computer daily. We compare this list to known vulnerabilities and updates. If any of your applications are at risk, we notify you and provide instructions on how to update the appropriate application.</p>
      <p><b>2. NEW APPLICATION MONITORING</b> – All newly installed applications are screened for suitability and acceptance. You are notified of any new application installed which seems to be out of the ordinary, so you are able to identify malicious software that has been installed. We also help catch nonapproved user installed applications.</p>
      <p><b>3. ANTI-VIRUS MONITORING</b> – Daily, each computer is checked for functioning and up-to-date anti-virus software.</p>
      <p><b>4. REALTIME INTERNET NAVIGATION AND SECURITY SERVICES</b> – Complementary to your anti-virus, this cloud-based service delivers real-time protection. Our web filtering service blocks access to malicious and phishing sites as they appear, stopping threats before they ever reach your network or the people working on it.</p>
      <p>If one of your computers becomes infected, the botnet protection stops it from sending data out of your office, limiting the damage and alerting us so we can respond quickly.</p>
      <p>Web content filtering is also provided, allowing access to a rich database of more than 80 categories, so you decide which sites are appropriate for your staff and your business.</p>
      <p><b>5. SECURITY AWARENESS PROGRAM</b> – Your staff is the core of your security strength or its weakest link. We provide a program to help educate your staff on how to spot threats, avoid risky behavior and keep your client information safe every day.</p>
    </section>
  </main>
</body>
</html>
```